Core values in our company OTK (Oversight and Transit Keepers)

Do good:
1. Being Direct and communicative for the benefit of all parties
2. Working for the Benefit of the company, client and team members
3. Wanting to improve to create a better impact
4. Having healthy rivalry
Be ahead of curve:
1. Having the confidence to break through barriers which arise
2. Desire to grow and learn towards establishment and agreed goal
3. Getting off the sidelines and get into the game
4. Keeping the end game in mind having due regard to processes and milestones
5. Self starter and works on own initiative
6. Diligent and impactful in your field of responsibility
Truth and Honesty
2. Have the confidence and ability to speak what you really want to communicate
3. Being truthful to yourself, clients and colleagues to find the innovations that lie within
4. Seeking the truth by opening things up for discussion
5. Being Optimistic
Background Information on our Company:OTK is a professional law firm in London Docklands. We caters for both private and corporate clients ranging from highly regarded and established law firms to boutique and niche immigration practices. We also specialises in expert legal advice and prides itself on providing services that go beyond the expectations of its clients.
What we need: We need a Poster about Truth and Honesty, this is to show one of our values as a company. It will need to be vibrant and straight to the point. Colours can be orange grey white and yellow. Attached is our company logo.
Reason: To remind colleagues that this is one of our main values and it is instilled in our company.
Things we would like:
1. To create a point of focus
2. Use shapes to create visual interest
3. Use creative illustrations
4. Take the viewer’s focus on a journey with clever perspective
Industry/Entity Type
Legal
Requirements
Must have
- a globe (Picture)
- Do good:
- 1. Being Direct and communicative for the benefit of all parties
- 2. Working for the Benefit of the company, client and team members
- 3. Wanting to improve to create a better impact
- 4. Having healthy rivalry
- Be ahead of curve:
- 1. Having the confidence to break through barriers which arise
- 2. Desire to grow and learn towards establishment and agreed goal
- 3. Getting off the sidelines and get into the game
- 4. Keeping the end game in mind having due regard to processes and milestones
- 5. Self starter and works on own initiative
- 6. Diligent and impactful in your field of responsibility
- Truth and Honesty
- 2. Have the confidence and ability to speak what you really want to communicate
- 3. Being truthful to yourself, clients and colleagues to find the innovations that lie within
- 4. Seeking the truth by opening things up for discussion
- 5. Being Optimistic

```html
<!DOCTYPE html>
<html lang="en">
<head>
<meta charset="utf-8">
<title>OTK Core Values Poster</title>
<link href="https://fonts.googleapis.com/css2?family=Oswald:wght@400;500&family=Roboto+Condensed:wght@400;700&display=swap" rel="stylesheet">
<style>
  :root {
    --stage: #efe3c2;
    --cream: #fdf6df;
    --cream-deep: #f8e6a8;
    --orange: #f39200;
    --orange-deep: #e8760e;
    --gold: #f7b500;
    --charcoal: #2e2e2e;
    --ink: #1d1d1d;
    --photo-warm-a: #c98f5c;
    --photo-warm-b: #6e3b2a;
    --photo-grey-a: #e9e7e4;
    --photo-grey-b: #bdb9b4;
    --photo-teal-a: #5f7a76;
    --photo-teal-b: #2f4744;
  }
  * { box-sizing: border-box; margin: 0; padding: 0; }
  html, body { width: 1200px; height: 640px; overflow: hidden; }
  body { background: var(--stage); position: relative; font-family: "Roboto Condensed", Arial, sans-serif; }

  .poster {
    position: absolute; left: 373px; top: 0;
    width: 454px; height: 640px;
    display: flex;
    box-shadow: 0 0 18px rgba(0,0,0,.12);
  }
  .values-column {
    width: 259px; height: 100%; position: relative;
    background: linear-gradient(180deg, var(--cream-deep) 0%, var(--cream) 35%, #fffbef 70%, var(--cream) 100%);
  }
  .photo-column { width: 195px; height: 100%; display: flex; flex-direction: column; gap: 2px; background: #fff; }
  .photo { flex: none; width: 100%; }
  .photo--shopping { height: 229px; background: linear-gradient(160deg, var(--photo-warm-a), var(--photo-warm-b)); }
  .photo--curve { height: 201px; background: linear-gradient(180deg, var(--photo-grey-a), var(--photo-grey-b)); }
  .photo--poster { height: 206px; background: linear-gradient(180deg, var(--photo-teal-a), var(--photo-teal-b)); }

  .brand {
    position: absolute; left: 76px; top: 30px;
    display: flex; align-items: center; gap: 8px;
    color: var(--charcoal); font-weight: 700;
  }
  .brand-mark { width: 20px; height: 20px; background: var(--orange); }
  .brand-name { font-size: 44px; line-height: 1; letter-spacing: 1px; }
  .brand-tagline {
    position: absolute; left: 60px; top: 80px; width: 170px; text-align: center;
    font-size: 10px; color: var(--charcoal); font-weight: 700;
  }

  .value { position: absolute; left: 20px; right: 8px; }
  .value--good { top: 127px; }
  .value--curve { top: 268px; }
  .value--truth { top: 453px; }

  .value-tag {
    display: inline-block; position: relative;
    font-family: "Oswald", "Arial Narrow", sans-serif; font-weight: 400;
    font-size: 19px; line-height: 25px; padding: 0 7px; border-radius: 7px;
    color: #fff; margin-left: 6px;
  }
  .value-tag::after {
    content: ""; position: absolute; left: 12px; bottom: -6px;
    border-left: 5px solid transparent; border-right: 5px solid transparent;
    border-top: 6px solid var(--tag-bg);
  }
  .value--good .value-tag { --tag-bg: var(--orange-deep); background: var(--orange-deep); }
  .value--curve .value-tag { --tag-bg: var(--gold); background: var(--gold); }
  .value--truth .value-tag { --tag-bg: var(--charcoal); background: var(--charcoal); }

  .value-list {
    list-style: none; margin-top: 10px; position: relative; padding-left: 18px;
    --bullet: var(--orange);
  }
  .value--curve .value-list { --bullet: var(--gold); }
  .value--truth .value-list { --bullet: var(--charcoal); }
  .value-list::before {
    content: ""; position: absolute; left: 3px; top: 6px; bottom: 6px;
    width: 1px; background: var(--bullet);
  }
  .value-list li {
    position: relative; font-size: 10.5px; line-height: 12.5px;
    color: var(--ink); margin-bottom: 4.5px;
  }
  .value-list li::before {
    content: ""; position: absolute; left: -18px; top: 2.5px;
    width: 7px; height: 7px; background: var(--bullet);
  }
</style>
</head>
<body>
  <main class="poster">
    <section class="values-column">
      <div class="brand">
        <span class="brand-mark"></span>
        <span class="brand-name">OTK</span>
      </div>
      <p class="brand-tagline">Oversight and Transit Keepers</p>

      <div class="value value--good">
        <h2 class="value-tag">DO GOOD:</h2>
        <ul class="value-list">
          <li>Being Direct and communicative for the benefit of all parties</li>
          <li>Working for the Benefit of the company, client and team members</li>
          <li>Wanting to improve to create a better impact</li>
          <li>Having healthy rivalry</li>
        </ul>
      </div>

      <div class="value value--curve">
        <h2 class="value-tag">Be a Head of Curve:</h2>
        <ul class="value-list">
          <li>Having the confidence to break through barriers which arise</li>
          <li>Desire to grow and learn towards establishment and agreed goal</li>
          <li>Getting off the sidelines and get into the game</li>
          <li>Keeping the end game in mind having due regard to processes and milestones</li>
          <li>Self starter and works on own initiative</li>
          <li>Diligent and impactful in your field of responsibility</li>
        </ul>
      </div>

      <div class="value value--truth">
        <h2 class="value-tag">Truth and Honesty</h2>
        <ul class="value-list">
          <li>Having the confidence to break through barriers which arise</li>
          <li>Have the confidence and ability to speak what you really want to communicate</li>
          <li>Being truthful to yourself, clients and colleagues to find the innovations that lie within</li>
          <li>Seeking the truth by opening things up for discussion</li>
          <li>Being Optimistic</li>
        </ul>
      </div>
    </section>

    <aside class="photo-column">
      <div class="photo photo--shopping" role="img" aria-label="Photo of a smiling woman in sunglasses holding two shopping bags printed with Do Good"></div>
      <div class="photo photo--curve" role="img" aria-label="Photo of a man in glasses beneath a hand-drawn bell curve with arrows pointing inward"></div>
      <div class="photo photo--poster" role="img" aria-label="Photo of a street poster reading Love Truth Again with a figure raising a hand"></div>
    </aside>
  </main>
</body>
</html>
```